Brightford Lingua Partners, LLC

We need a business card that includes information about our business and conveys a reliable business that provides document translation services and interpreters for a variety of corporate and individual clients. We want to come across as professional, reliable, yet approachable. It should include the following on one side:

ESL / ENL Language Classes, Private Lessons, and Online Tutors
PALQE Training and Testing
Translating & Interpreting Services
Contact us about Over-the-Phone Interpreting in over 200 languages
24/7/365
www.brightfordlingua.example

The other side should include (555) 481-3062

Marla Quennick, President
412 Garvin Ave., Ste. 209
Indianapolis, IN 46999
Updates

Please add USA as part of the address. Also, please add mrqquennick@brightfordlinguapartners.example as the e-mail address. Thank you.

Target Market(s)

Business professionals, their families, the international community

Industry/Entity Type

Business

Contact Information for Business Card

24/7/365
www.brightfordlingua.example

(555) 481-3062

Marla Quennick, President
412 Garvin Ave., Ste. 209
Indianapolis, IN 46999
USA

Font styles to use
Sans Serif

Colors

Designer to choose colors to be used in the design.

Requirements
Must have
• See project description
• e-mail address and web address
• Phone number
Nice to have
• a globe
• physical address
Should not have
• Should not have the same color scheme as other agencies in our market in Indiana unless it is blue and black. No purple or yellow.

```html
<!DOCTYPE html>
<html lang="en">
<head>
<meta charset="utf-8">
<title>Brightford Lingua Partners, LLC – Business Card</title>
<link rel="stylesheet" href="https://fonts.googleapis.com/css2?family=Open+Sans:wght@400;600&display=swap">
<style>
  :root {
    --bg: #4a4a4c;
    --card-white: #ffffff;
    --ink: #1d1d1f;
    --brand-blue: #1c8ad8;
    --blue-light: #2f9be6;
    --blue-deep: #0f5fb0;
    --blue-darker: #0b4c93;
    --on-blue: #ffffff;
  }
  * { margin: 0; padding: 0; box-sizing: border-box; }
  html, body { width: 1200px; height: 900px; overflow: hidden; }
  body {
    background: var(--bg);
    font-family: "Open Sans", Arial, sans-serif;
    display: flex;
    flex-direction: column;
    align-items: center;
    justify-content: center;
    gap: 36px;
  }
  .card {
    position: relative;
    width: 700px;
    height: 400px;
    border-radius: 34px;
    overflow: hidden;
  }

  /* ---------- Front (white) ---------- */
  .card-front { background: var(--card-white); color: var(--ink); }
  .brand {
    position: absolute;
    display: flex;
    align-items: center;
    gap: 14px;
  }
  .brand-dot {
    width: 92px; height: 92px;
    border-radius: 50%;
    background: var(--brand-blue);
    flex: none;
  }
  .brand-name {
    font-size: 27px;
    line-height: 1.08;
    font-weight: 400;
  }
  .card-front .brand { left: 56px; top: 64px; }
  .card-front .brand-name { color: var(--ink); }

  .person { position: absolute; left: 380px; top: 60px; }
  .person-name { font-size: 30px; font-weight: 400; letter-spacing: 0.5px; }
  .person-title { font-size: 16px; color: var(--brand-blue); margin-top: -4px; }
  .rule { width: 80px; height: 3px; background: var(--brand-blue); margin-top: 14px; }

  .contact-list { position: absolute; left: 262px; top: 188px; list-style: none; }
  .contact-list li {
    display: flex; align-items: center; gap: 10px;
    font-size: 15px; line-height: 30px; white-space: nowrap;
  }
  .contact-list svg { width: 16px; height: 16px; fill: var(--brand-blue); flex: none; }
  .contact-rule { position: absolute; left: 262px; top: 298px; width: 80px; height: 3px; background: var(--brand-blue); }

  .address {
    position: absolute; left: 56px; bottom: 40px;
    display: flex; align-items: center; gap: 8px;
    font-size: 15px; white-space: nowrap;
  }
  .address svg { width: 14px; height: 18px; fill: var(--brand-blue); flex: none; }

  /* ---------- Back (blue) ---------- */
  .card-back {
    background: linear-gradient(160deg, var(--blue-light) 0%, var(--brand-blue) 45%, var(--blue-deep) 100%);
    color: var(--on-blue);
  }
  .globe-area {
    position: absolute;
    left: 120px; top: -120px;
    width: 460px; height: 460px;
    border-radius: 50%;
    background: radial-gradient(circle at 45% 45%, rgba(255,255,255,0.10) 0%, rgba(11,76,147,0.55) 70%, rgba(11,76,147,0.75) 100%);
  }
  .card-back .brand { left: 200px; top: 66px; }
  .card-back .brand-dot { background: rgba(255,255,255,0.85); width: 100px; height: 100px; }
  .card-back .brand-name { color: var(--on-blue); font-size: 29px; }

  .services {
    position: absolute; left: 0; right: 0; top: 222px;
    text-align: center;
    font-size: 16px; line-height: 27px;
  }
  .services .sep { padding: 0 10px; }
</style>
</head>
<body>

  <section class="card card-front" aria-label="Business card front">
    <div class="brand">
      <span class="brand-dot"></span>
      <span class="brand-name">Brightford<br>Lingua<br>Partners, LLC</span>
    </div>

    <div class="person">
      <p class="person-name">Your Name</p>
      <p class="person-title">Job Title</p>
      <div class="rule"></div>
    </div>

    <ul class="contact-list">
      <li>
        <svg viewBox="0 0 16 16" aria-hidden="true"><path d="M3 1.5l3 .5 1 3-1.8 1.3a9 9 0 0 0 4.5 4.5L11 9l3 1 .5 3-1.7 1.5C7 14.5 1.5 9 1.5 3.2z"/></svg>
        (555) 481-3062
      </li>
      <li>
        <svg viewBox="0 0 16 16" aria-hidden="true"><path d="M1 3h14v10H1zM2.2 4.2v.4L8 9l5.8-4.4v-.4z"/></svg>
        mrqquennick@brightfordlinguapartners.example
      </li>
      <li>
        <svg viewBox="0 0 16 16" aria-hidden="true"><path d="M8 1a7 7 0 1 0 0 14A7 7 0 0 0 8 1zm0 1.3c.9 0 1.9 1.8 2.1 4.2H5.9C6.1 4.1 7.1 2.3 8 2.3zM2.4 7.5h2.2c0 .4 0 .7.1 1H2.4zm0 1.5h2.3c.2 1.5.6 2.8 1.2 3.7A5.7 5.7 0 0 1 2.4 9zm3.5 0h4.2c-.2 2.4-1.2 4.7-2.1 4.7S6.1 11.4 5.9 9zm5.4 0h2.3a5.7 5.7 0 0 1-3.5 3.7c.6-.9 1-2.2 1.2-3.7zm2.3-1.5h-2.2v-1h2.2zM11.3 5.5a8 8 0 0 0-1.2-3.2 5.7 5.7 0 0 1 3.5 3.2zM5.9 2.3A8 8 0 0 0 4.7 5.5H2.4a5.7 5.7 0 0 1 3.5-3.2z"/></svg>
        www.brightfordlingua.example
      </li>
    </ul>
    <div class="contact-rule"></div>

    <p class="address">
      <svg viewBox="0 0 14 18" aria-hidden="true"><path d="M7 0a6 6 0 0 0-6 6c0 4.5 6 12 6 12s6-7.5 6-12a6 6 0 0 0-6-6zm0 8.5A2.5 2.5 0 1 1 7 3.5a2.5 2.5 0 0 1 0 5z"/></svg>
      Marla Quennick, President, 412 Garvin Ave., Ste. 209, Indianapolis, IN 46999, USA
    </p>
  </section>

  <section class="card card-back" aria-label="Business card back">
    <div class="globe-area" role="img" aria-label="Large soft globe with world continents behind the brand name"></div>

    <div class="brand">
      <span class="brand-dot"></span>
      <span class="brand-name">Brightford<br>Lingua<br>Partners, LLC</span>
    </div>

    <div class="services">
      <p>ESL / ENL Language Classes, Private Lessons and Online Tutors</p>
      <p>PALQE Training and Testing<span class="sep">/</span>Translating &amp; Interpreting Services</p>
      <p>Contact us about Over-the-Phone Interpreting in over 200 languages 24/7/365</p>
    </div>
  </section>

</body>
</html>
```